Quillon Maison Wood Fired Pizza business card design

I have a logo and need an eye catching design that will get me noticed.
My business is wood fired pizza. I want a bold design that will make our customers remember us and the food that we serve. Work with the colors of our logo and texts. Maybe add designs that lend to what or how pizza is made using our wood fired oven?

Target Market(s)

Foodies!

Contact Information for Business Card

Quillon Maison Wood Fired Pizza
Our slogan is Fast. Fresh. Handcrafted
Catering for all events

Requirements
Must have
• Dana Porrick
Telephone 570 555 0183
website www.getquillon.example
Facebook @getquillonpizza maybe use the facebook logo next to it
Instagram getquillonpizza maybe use the instagram logo next to it
Catering for all events
Nice to have
• Maybe pizza peels, pizza cutters? Wood? Fired wood? Using our flame in the background?
Please work with different colored text so each sentence stands out? A themed color for facebook?
Maybe work with the colors within our logo?
Please try to use the our quillon font, but not a must have.

```html
<!DOCTYPE html>
<html lang="en">
<head>
<meta charset="utf-8">
<title>Quillon Maison Wood Fired Pizza – Business Card</title>
<link href="https://fonts.googleapis.com/css2?family=Open+Sans:wght@400;600;700;800&display=swap" rel="stylesheet">
<style>
  :root {
    --page: #2a2b2e;
    --card: #131722;
    --ink-white: #f4f4f4;
    --ink-soft: #c9ccd3;
    --accent-red: #d42027;
    --accent-orange: #f0901e;
    --flame-deep: #182033;
    --flame-light: #2f3f62;
  }
  * { margin: 0; padding: 0; box-sizing: border-box; }
  html, body {
    width: 1200px; height: 900px; overflow: hidden;
    background: var(--page);
    font-family: "Open Sans", sans-serif;
  }
  .sheet {
    width: 1200px; height: 900px;
    display: flex; flex-direction: column; align-items: center; justify-content: center;
    gap: 36px;
  }
  .card {
    position: relative;
    width: 680px; height: 389px;
    background: var(--card);
    box-shadow: 0 10px 28px rgba(0,0,0,.45);
    overflow: hidden;
  }

  /* brand lockup shared by both sides */
  .lockup {
    display: flex; flex-direction: column; align-items: center;
    color: var(--ink-white);
  }
  .lockup-tagline {
    font-size: 11px; font-weight: 700; letter-spacing: 2px;
    text-transform: uppercase; color: var(--ink-white);
  }
  .lockup-rule {
    width: 100%; height: 2px; background: var(--accent-orange); margin: 6px 0;
  }
  .lockup-name {
    display: flex; align-items: center; gap: 10px;
    font-weight: 800; font-size: 30px; letter-spacing: 3px;
    text-transform: uppercase; line-height: 1;
  }
  .lockup-dot {
    width: 14px; height: 14px; border-radius: 50%;
    background: var(--accent-orange); flex: none;
  }
  .lockup-est {
    font-size: 9px; font-weight: 600; letter-spacing: 2px; color: var(--ink-white);
  }

  /* front */
  .card-front .lockup {
    position: absolute; left: 40px; top: 130px; width: 270px;
  }
  .divider {
    position: absolute; left: 338px; top: 70px; width: 1px; height: 250px;
    background: var(--accent-orange);
  }
  .contact {
    position: absolute; left: 366px; top: 88px;
  }
  .contact-name {
    color: var(--accent-red); font-weight: 700; font-size: 26px;
    text-transform: uppercase; letter-spacing: .5px; margin-bottom: 20px;
  }
  .contact-list { list-style: none; }
  .contact-list li {
    display: flex; align-items: center; gap: 10px;
    color: var(--ink-white); font-size: 18px; line-height: 28px;
  }
  .contact-list svg { width: 17px; height: 17px; flex: none; }
  .contact-extra {
    margin-top: 18px; font-size: 13px; line-height: 20px;
  }
  .contact-slogan { color: var(--accent-orange); font-weight: 700; letter-spacing: 1px; text-transform: uppercase; }
  .contact-catering { color: var(--ink-soft); }

  /* back */
  .flame-field {
    position: absolute; left: 30px; top: 0; width: 360px; height: 389px;
    background: linear-gradient(180deg, var(--flame-deep) 0%, var(--flame-light) 100%);
    border-radius: 60% 40% 48% 52% / 70% 60% 40% 30%;
    opacity: .85;
  }
  .card-back .lockup {
    position: absolute; right: 40px; bottom: 56px; width: 330px;
  }
</style>
</head>
<body>
<main class="sheet">
  <section class="card card-front">
    <div class="lockup">
      <span class="lockup-tagline">Wood Fired Pizza</span>
      <span class="lockup-rule"></span>
      <span class="lockup-name"><span class="lockup-dot"></span>Quillon Maison</span>
      <span class="lockup-rule"></span>
      <span class="lockup-est">EST. 2020</span>
    </div>
    <div class="divider"></div>
    <div class="contact">
      <p class="contact-name">Dana Porrick</p>
      <ul class="contact-list">
        <li>
          <svg viewBox="0 0 20 20"><path d="M5 2l3 4-2 2c1 2.5 3 4.5 5.5 5.5l2-2 4 3-2 3C9 17 3 11 2 5z" fill="var(--accent-orange)"/></svg>
          570 555 0183
        </li>
        <li>
          <svg viewBox="0 0 20 20" fill="none" stroke="var(--accent-orange)" stroke-width="1.8"><circle cx="10" cy="10" r="8"/><path d="M2 10h16M10 2c-3 3-3 13 0 16M10 2c3 3 3 13 0 16"/></svg>
          www.getquillon.example
        </li>
        <li>
          <svg viewBox="0 0 20 20"><rect x="2" y="2" width="16" height="16" rx="3" fill="var(--accent-orange)"/></svg>
          @getquillonpizza
        </li>
        <li>
          <svg viewBox="0 0 20 20"><circle cx="10" cy="10" r="8" fill="var(--accent-orange)"/></svg>
          getquillonpizza
        </li>
      </ul>
      <div class="contact-extra">
        <p class="contact-slogan">Fast. Fresh. Handcrafted.</p>
        <p class="contact-catering">Catering for all events</p>
      </div>
    </div>
  </section>

  <section class="card card-back">
    <div class="flame-field" role="img" aria-label="Large embossed flame decoration in deep navy tones"></div>
    <div class="lockup">
      <span class="lockup-tagline">Wood Fired Pizza</span>
      <span class="lockup-rule"></span>
      <span class="lockup-name"><span class="lockup-dot"></span>Quillon Maison</span>
      <span class="lockup-rule"></span>
      <span class="lockup-est">EST. 2020</span>
    </div>
  </section>
</main>
</body>
</html>
```